Film and TV production company

I have the logo already designed by mark quarry. I just need the text and the logo attached to the business card. Maybe a small design on the back of the card or text.

Industry/Entity Type

film tv arts

Contact Information for Business Card

Dale Morrow Cinematographer-Director

Colors
F0912C
F2A743
F7CA91
FBE8D2
FDF5EE
EE7325
F08F49
F5BC92
FAE3D3
FDF4ED

Requirements
Must have
• www.copperlanepix.com.au my email address mail@copperlanepix.com.au my mobile number 0491570158
Nice to have
• Some kind of small art work on the back that ties in with the logo design attached
Should not have
• Must clean and simple

```html
<!DOCTYPE html>
<html lang="en">
<head>
<meta charset="utf-8">
<title>Copper Lane Pictures – Business Card</title>
<link href="https://fonts.googleapis.com/css2?family=Montserrat:wght@300&family=Arimo:wght@400;700&display=swap" rel="stylesheet">
<style>
  :root {
    --bg: #2a2a2a;
    --card-dark: #1f1f1f;
    --orange: #e67f22;
    --gold: #c2a064;
    --tan: #c3a26a;
    --brown: #8a5722;
    --forest: #3f4f24;
    --leaf: #67a040;
    --slate: #4b6277;
    --mist: #a8b3be;
    --white: #ffffff;
  }
  * { margin: 0; padding: 0; box-sizing: border-box; }
  html, body { width: 1200px; height: 900px; overflow: hidden; background: var(--bg); }
  .canvas {
    width: 1200px; height: 900px;
    display: flex; flex-direction: column; align-items: center; justify-content: center; gap: 56px;
  }
  .card {
    position: relative; width: 560px; height: 320px; border-radius: 18px; overflow: hidden;
    box-shadow: 0 12px 30px rgba(0,0,0,.45);
  }

  /* Front */
  .card--front { background: var(--card-dark); }
  .brand {
    position: absolute; right: 44px; top: 40px;
    display: flex; flex-direction: column; align-items: flex-end; gap: 12px;
  }
  .brand__dot { width: 78px; height: 78px; border-radius: 50%; background: var(--orange); margin-right: 20px; }
  .brand__name {
    font-family: 'Montserrat', sans-serif; font-weight: 300; color: var(--white);
    font-size: 20px; letter-spacing: 4px; white-space: nowrap; text-transform: uppercase;
  }
  .person { position: absolute; left: 40px; top: 200px; }
  .person__name {
    font-family: 'Arimo', sans-serif; font-weight: 700; color: var(--gold);
    font-size: 21px; text-transform: uppercase; white-space: nowrap;
  }
  .person__role { font-family: 'Arimo', sans-serif; color: var(--white); font-size: 14px; margin-top: 2px; white-space: nowrap; }
  .divider { position: absolute; left: 232px; top: 194px; width: 1px; height: 76px; background: var(--gold); }
  .contacts { position: absolute; left: 254px; top: 196px; list-style: none; }
  .contacts li {
    display: flex; align-items: center; gap: 8px; font-family: 'Arimo', sans-serif;
    color: var(--white); font-size: 14px; height: 25px; white-space: nowrap;
  }
  .contacts svg { width: 14px; height: 14px; fill: var(--orange); flex: none; }
  .edge-bands { position: absolute; left: 0; right: 0; bottom: 0; height: 12px; display: flex; }
  .edge-bands span { flex: 1; }
  .edge-bands .b1 { background: var(--orange); }
  .edge-bands .b2 { background: var(--tan); }
  .edge-bands .b3 { background: var(--brown); }
  .edge-bands .b4 { background: var(--forest); }
  .edge-bands .b5 { background: var(--leaf); }
  .edge-bands .b6 { background: var(--slate); }
  .edge-bands .b7 { background: var(--mist); }

  /* Back */
  .card--back { background: var(--orange); }
  .back__name {
    position: absolute; left: 44px; top: 44px;
    font-family: 'Montserrat', sans-serif; font-weight: 300; color: var(--white);
    font-size: 38px; letter-spacing: 8px; line-height: 1.3; text-transform: uppercase;
    white-space: nowrap;
  }
  .back__art {
    position: absolute; left: 0; right: 0; bottom: 0; height: 150px;
    background: linear-gradient(180deg, var(--forest) 0%, #4a4a22 100%);
  }
</style>
</head>
<body>
<main class="canvas">
  <section class="card card--front" aria-label="Card front">
    <div class="brand">
      <div class="brand__dot"></div>
      <p class="brand__name">Copper Lane Pictures</p>
    </div>
    <div class="person">
      <p class="person__name">Dale Morrow</p>
      <p class="person__role">Cinematographer-Director</p>
    </div>
    <div class="divider"></div>
    <ul class="contacts">
      <li><svg viewBox="0 0 24 24"><path d="M6.6 10.8a15 15 0 0 0 6.6 6.6l2.2-2.2a1 1 0 0 1 1-.25 11.4 11.4 0 0 0 3.6.57 1 1 0 0 1 1 1V20a1 1 0 0 1-1 1A17 17 0 0 1 3 4a1 1 0 0 1 1-1h3.5a1 1 0 0 1 1 1c0 1.25.2 2.45.57 3.57a1 1 0 0 1-.25 1z"/></svg>0491570158</li>
      <li><svg viewBox="0 0 24 24"><path d="M2 5h20v14H2z M2 5l10 8 10-8" stroke="#1f1f1f" stroke-width="1.5"/></svg>mail@copperlanepix.com.au</li>
      <li><svg viewBox="0 0 24 24"><circle cx="12" cy="12" r="10"/><path d="M2 12h20M12 2c3 3 3 17 0 20M12 2c-3 3-3 17 0 20" stroke="#1f1f1f" stroke-width="1.5" fill="none"/></svg>www.copperlanepix.com.au</li>
    </ul>
    <div class="edge-bands"><span class="b1"></span><span class="b2"></span><span class="b3"></span><span class="b4"></span><span class="b5"></span><span class="b6"></span><span class="b7"></span></div>
  </section>

  <section class="card card--back" aria-label="Card back">
    <p class="back__name">Copper Lane<br>Pictures</p>
    <div class="back__art" role="img" aria-label="Artwork area in deep forest green and earth tones"></div>
  </section>
</main>
</body>
</html>
```